Security and Staff Identity Business Products Brochure is required.

Looking for a brochure that introduces the business, and the general products and categories we sell.

The flyer will be 2 sided A3 in size, which will be folded in half once printed to effectively be 4 printed sides. 420 x 297mm

I have a pixel-vault account - if there is images you would like to use and i like the design i can purchase them.

As the finalised contact details have not yet available, please ensure that the final contact design can be edited for contact details - Phone, address, email etc.

Content is in the attached files. Ideally the front page will have logo, image/s, and our 3x Value pillars "Global Brands", "Local Supply", "Expert Advice".
Inside will have the 4 product lines w/ content and relevant images.

I have attached an similar brochure for the idea - Titles Tavonn Brochure. PLEASE Note i am after a far more sophisticated and professional looking brochure than this.

Target Market(s)

Potential new customers who need to be introduced to who we are and what range of products we supply

Industry/Entity Type

Security

Font styles to use
Other font styles liked:
• Calibri

Colors
abd037
ffffff
919191
1b1b1b
474747
9bcb3c

Requirements
Must have
• Must have 4 categories shown on the inside page/s. Printers, Printer Ribbons, Cards & Access, and Accessories.
• Show the supplier logo's we supply.
• Some not necessarily all corresponding images to those categories.
• Text content in the IDbrochure.docx attachment.
• Must be: 2 sided A3 in size, which will be folded in half once printed to effectively be 4 printed sides. 420 x 297mm
• x Value pillars "Global Brands", "Local Supply", "Expert Advice"
• Colours as per business card and logo design attached.
Nice to have
• Nice to have some background images from Pixel Vault or similar. Business people walking through a business environment.
Should not have
• No cartoons

```html
<!DOCTYPE html>
<html lang="en">
<head>
<meta charset="utf-8">
<title>Badgewell Brochure</title>
<link href="https://fonts.googleapis.com/css2?family=Open+Sans:wght@400;600&family=Montserrat:wght@400;600&display=swap" rel="stylesheet">
<style>
  :root {
    --green: #83c341;
    --green-dark: #6fae2f;
    --grey: #919191;
    --grey-mid: #474747;
    --ink: #1b1b1b;
    --white: #ffffff;
    --paper: #e6e6e6;
    --rule: #c9c9c9;
  }
  * { box-sizing: border-box; margin: 0; padding: 0; }
  html, body { width: 893px; height: 1200px; overflow: hidden; }
  body { background: var(--paper); font-family: "Open Sans", sans-serif; color: var(--grey-mid); position: relative; }

  .sheet { position: absolute; left: 56px; width: 766px; height: 542px; background: var(--white); overflow: hidden; box-shadow: 0 2px 4px rgba(0,0,0,.25); }
  .sheet--inside { top: 44px; }
  .sheet--outside { top: 625px; }

  /* inside */
  .side-rail { position: absolute; left: 0; top: 0; width: 143px; height: 542px; background: var(--ink); }
  .rail-mark { position: absolute; left: 0; top: -20px; width: 128px; height: 128px; border-radius: 50%; background: #3a3a3a; }
  .product-photo { position: absolute; left: 24px; width: 96px; height: 96px; border-radius: 50%; border: 3px solid var(--green); background: radial-gradient(circle at 50% 45%, #f2f2f2, #bdbdbd); }

  .brand { position: absolute; display: flex; align-items: center; }
  .brand-dot { border-radius: 50%; background: var(--green); flex: none; }
  .brand-name { font-family: "Open Sans", sans-serif; font-weight: 600; color: var(--green); line-height: 1; letter-spacing: -0.5px; }
  .brand-tag { position: absolute; color: var(--grey-mid); white-space: nowrap; }

  .brand--inside { left: 160px; top: 28px; }
  .brand--inside .brand-dot { width: 28px; height: 28px; margin-right: 6px; }
  .brand--inside .brand-name { font-size: 25px; }
  .brand-tag--inside { left: 201px; top: 54px; font-size: 7.4px; }

  .copy { position: absolute; left: 164px; width: 195px; }
  .copy h2 { font-size: 9.6px; font-weight: 600; color: var(--green); text-transform: uppercase; margin-bottom: 4px; }
  .copy p { font-size: 5.9px; line-height: 1.42; text-align: justify; color: #333; margin-bottom: 4px; }

  .right-panel { position: absolute; left: 383px; top: 0; width: 383px; height: 420px; background: linear-gradient(90deg, #f2f2f2, #ffffff 60%); }
  .reader-photo { position: absolute; left: 36px; top: 28px; width: 154px; height: 132px; border-radius: 6px; background: linear-gradient(135deg, #dcdcdc, #3a3a3a 55%, #f0f0f0); }
  .cards-copy { left: 198px; top: 46px; width: 153px; }
  .cards-copy h2 { line-height: 1.25; }

  .partners-title { position: absolute; left: 0; top: 194px; width: 383px; text-align: center; font-family: "Montserrat", sans-serif; }
  .partners-title .lead { font-size: 12px; color: var(--grey-mid); display: block; }
  .partners-title .strong { font-size: 12px; font-weight: 600; color: var(--green); display: block; margin-top: 1px; }
  .partner-box { position: absolute; left: 22px; top: 234px; width: 339px; height: 56px; border: 1px solid var(--rule); display: flex; justify-content: space-around; align-items: center; padding: 0 14px; }
  .partner-badge { width: 52px; height: 16px; border-radius: 2px; }

  .pillar { position: absolute; top: 310px; width: 90px; text-align: center; font-family: "Montserrat", sans-serif; }
  .pillar svg { display: block; margin: 0 auto 4px; }
  .pillar .lead { display: block; font-size: 12.5px; color: var(--grey-mid); line-height: 1.15; }
  .pillar .strong { display: block; font-size: 12.5px; font-weight: 600; color: var(--green); line-height: 1.2; }

  .strip { position: absolute; left: 143px; top: 420px; width: 623px; height: 74px; border-top: 1px solid var(--rule); background: #fafafa; }
  .strip-item { position: absolute; top: 10px; height: 56px; border-radius: 6px; }

  .contact-bar { position: absolute; left: 143px; top: 494px; width: 623px; height: 48px; background: var(--green); color: var(--white); font-family: "Montserrat", sans-serif; }
  .phone { position: absolute; left: 42px; top: 13px; display: flex; align-items: center; font-size: 13.5px; letter-spacing: .6px; }
  .phone svg { margin-right: 8px; }
  .web { position: absolute; left: 343px; top: 15px; font-size: 12.5px; letter-spacing: .8px; }

  /* outside */
  .header-band { position: absolute; left: 0; top: 0; width: 766px; height: 123px; }
  .brand--outside .brand-dot { width: 56px; height: 56px; margin-right: 10px; }
  .brand--outside .brand-name { font-size: 38px; }
  .brand-tag--outside { font-size: 13px; }
  .cover-panel { position: absolute; left: 0; top: 123px; width: 383px; height: 290px; background: var(--green); }
  .cover-panel h3 { position: absolute; left: 155px; top: 47px; color: var(--white); font-family: "Montserrat", sans-serif; font-weight: 400; font-size: 13.5px; letter-spacing: .8px; }
  .cover-photo { position: absolute; left: 383px; top: 123px; width: 383px; height: 290px; background: linear-gradient(110deg, #6a5a78 0%, #a89aa8 30%, #c9ccd2 60%, #dfe3e6 100%); }
  .footer-band { position: absolute; left: 0; top: 413px; width: 766px; height: 129px; background: var(--ink); }
  .footer-mark { position: absolute; left: -40px; top: 0; width: 210px; height: 210px; border-radius: 50%; background: #2f2f2f; }
  .categories { position: absolute; right: 24px; top: 26px; width: 380px; text-align: center; font-family: "Montserrat", sans-serif; font-weight: 600; font-size: 11.6px; color: var(--green); line-height: 1.5; }
  .footer-rule { position: absolute; left: 475px; top: 86px; width: 190px; border-top: 1px solid #5a5a5a; }
  .footer-web { position: absolute; left: 400px; top: 100px; width: 340px; text-align: center; color: #e0e0e0; font-family: "Montserrat", sans-serif; font-size: 13.5px; letter-spacing: 1px; }
</style>
</head>
<body>

<section class="sheet sheet--inside">
  <div class="side-rail">
    <div class="rail-mark"></div>
    <div class="product-photo" style="top:170px" role="img" aria-label="Compact ID card printer"></div>
    <div class="product-photo" style="top:288px" role="img" aria-label="Dual-sided ID card printer"></div>
    <div class="product-photo" style="top:406px" role="img" aria-label="Retransfer ID card printer"></div>
  </div>

  <div class="brand brand--inside"><span class="brand-dot"></span><span class="brand-name">Badgewell</span></div>
  <div class="brand-tag brand-tag--inside">Keeping your people and business secure</div>

  <div class="copy" style="top:88px">
    <h2>ID Card Printers</h2>
    <p>Whether you're looking for a plastic card printer for staff ID, membership cards, or secure access control cards we supply some of the world's leading brands of ID card printers. The brands we supply ensure our customers have the best quality solution and most reliable hardware available.</p>
    <p>With ID card systems from Badgewell you're taking a critical step to a more secure business environment. ID card solutions for all applications and budgets are readily available.</p>
  </div>

  <div class="copy" style="top:193px">
    <h2>Printer Ribbons &amp; Maintenance</h2>
    <p>We supply card printer ribbons for a range of different model card printers. Whether you're printing single sided, or double sided, colour or monochrome we have the print consumables and recommendations to suit.</p>
    <p>Talk to us today and let us help you out with selecting the right printer ribbons for your printer today.</p>
    <p>Plastic card printers require care and regular maintenance to ensure they operate at peak performance. Our cleaning kits will ensure the upkeep of your printer is an easy process.</p>
  </div>

  <div class="copy" style="top:313px">
    <h2>ID Accessories</h2>
    <p>Badgewell provide a wide range of options on card holders, lanyards, retractable card reels, clips and lapels.</p>
    <p>Made from high quality materials and readily available talk to us today and find out what makes us different to your existing supplier.</p>
    <p>We can customise your accessories with corporate logo's and branding on their ID card holders, lanyards and clips and zingers.</p>
  </div>

  <div class="right-panel">
    <div class="reader-photo" role="img" aria-label="Access card reader, phone credential, key fob and smart card"></div>
    <div class="copy cards-copy">
      <h2>Cards<br>&amp; Access Control</h2>
      <p>Badgewell supply genuine Corvane access control cards, if you're running an existing ProxLine, Smartline, Keyra or Vandel access control card solution, why not ask us today for quote.</p>
      <p>Looking for Key fobs or wristbands? We can help you out with the same level of expertise, advice and customer experience we pride ourselves on.</p>
    </div>

    <div class="partners-title">
      <span class="lead">Partnering with</span>
      <span class="strong">THE BEST MANUFACTURES IN THE WORLD</span>
    </div>
    <div class="partner-box">
      <span class="partner-badge" style="background:#1f4fa0"></span>
      <span class="partner-badge" style="background:#e04a3a"></span>
      <span class="partner-badge" style="background:#5a5a6a"></span>
      <span class="partner-badge" style="background:#2a4ea8"></span>
    </div>

    <div class="pillar" style="left:32px">
      <svg width="52" height="52" viewBox="0 0 52 52"><circle cx="26" cy="26" r="24" fill="#fff" stroke="var(--green)" stroke-width="2"/><circle cx="20" cy="21" r="5" fill="var(--grey)"/><circle cx="32" cy="21" r="5" fill="var(--grey)"/><path d="M11 37c0-6 4-9 9-9s9 3 9 9zM23 37c0-6 4-9 9-9s9 3 9 9z" fill="var(--grey)"/></svg>
      <span class="lead">Expert</span><span class="strong">ADVICE</span>
    </div>
    <div class="pillar" style="left:146px">
      <svg width="52" height="52" viewBox="0 0 52 52"><circle cx="26" cy="26" r="24" fill="#fff" stroke="var(--green)" stroke-width="2"/><g fill="none" stroke="var(--grey)" stroke-width="1.6"><circle cx="26" cy="26" r="13"/><ellipse cx="26" cy="26" rx="6" ry="13"/><path d="M13 26h26M15 20h22M15 32h22"/></g></svg>
      <span class="lead">Global</span><span class="strong">BRANDS</span>
    </div>
    <div class="pillar" style="left:258px">
      <svg width="52" height="52" viewBox="0 0 52 52"><circle cx="26" cy="26" r="24" fill="#fff" stroke="var(--green)" stroke-width="2"/><path d="M26 40c-6-8-10-13-10-18a10 10 0 0 1 20 0c0 5-4 10-10 18z" fill="var(--grey)"/><circle cx="26" cy="22" r="4" fill="#fff"/></svg>
      <span class="lead">Local</span><span class="strong">SUPPLY</span>
    </div>
  </div>

  <div class="strip">
    <div class="strip-item" style="left:30px;width:80px;background:linear-gradient(90deg,#3a2a5a,#c21e6a 45%,#f4e03a 75%,#444)" role="img" aria-label="Colour printer ribbon"></div>
    <div class="strip-item" style="left:150px;width:80px;background:linear-gradient(160deg,#9a9a9a,#5c5c5c)" role="img" aria-label="Grey staff lanyard"></div>
    <div class="strip-item" style="left:262px;width:82px;background:linear-gradient(90deg,#b0b0b0,#3e4ea0 40%,#c8c8c8 60%,#d33a2a)" role="img" aria-label="Retractable card reels"></div>
    <div class="strip-item" style="left:385px;width:80px;background:linear-gradient(135deg,#4aa84a,#d33a2a 50%,#2d4ea0)" role="img" aria-label="RFID wristbands"></div>
    <div class="strip-item" style="left:510px;width:70px;background:linear-gradient(135deg,#e6e6e6,#a6a6a6)" role="img" aria-label="Badge clip"></div>
  </div>

  <div class="contact-bar">
    <div class="phone">
      <svg width="22" height="22" viewBox="0 0 22 22"><circle cx="11" cy="11" r="10" fill="none" stroke="#fff" stroke-width="1.4"/><path d="M5 10c2-3 10-3 12 0l-2 2-2-1v-1h-4v1l-2 1z" fill="#fff"/><rect x="8" y="12" width="6" height="3" rx="1" fill="#fff"/></svg>
      + 000 000 000
    </div>
    <div class="web">www.badgewell.example</div>
  </div>
</section>

<section class="sheet sheet--outside">
  <div class="header-band">
    <div class="brand brand--outside" style="left:38px;top:33px"><span class="brand-dot"></span><span class="brand-name">Badgewell</span></div>
    <div class="brand-tag brand-tag--outside" style="left:104px;top:78px">Keeping your people and business secure</div>
    <div class="brand brand--outside" style="left:419px;top:33px"><span class="brand-dot"></span><span class="brand-name">Badgewell</span></div>
    <div class="brand-tag brand-tag--outside" style="left:485px;top:78px">Keeping your people and business secure</div>
  </div>

  <div class="cover-panel"><h3>CONTACT</h3></div>
  <div class="cover-photo" role="img" aria-label="Business woman smiling in a modern office corridor with colleagues behind"></div>

  <div class="footer-band">
    <div class="footer-mark"></div>
    <div class="categories">· ID CARD PRINTERS · PRINTER RIBBONS<br>· MAINTENANCE &nbsp;· ACCESS CONTROL · ID ACCESSORIES</div>
    <div class="footer-rule"></div>
    <div class="footer-web">www.badgewell.example</div>
  </div>
</section>

</body>
</html>
```